Business Card - Rebranding for Consulting Firm

We are renaming and rebranding our consulting firm and need to raise the level of quality of our cards as part of that effort. We consult to leading high tech, life science and other innovation sector companies.

Need a two-sided business card design.

Side 1: (a) Company logo (b) tag line: Optimize Your Investment in Talent (c) Name (d) Title (e) Phone 1: Office (f) Phone 2: Mobile (g) email: person@HollowmereAdvisory.com

Side 2: Two lines of text: (a) Growth is Imperative. Change is Constant. Talent Executes Strategy. (b) We help you excel at all three.

Target Market(s)

Business and human resources executives and senior managers

Industry/Entity Type

Management Consulting

Contact Information for Business Card

Font styles to use
Sans Serif

Requirements
Must have
• clean, not too busy, but with a bit of creativity. Stick to the colors used in the attached logo
• appeal to high tech, life science companies
Nice to have
• prefer white background

```html
<!DOCTYPE html>
<html lang="en">
<head>
<meta charset="utf-8">
<title>Hollowmere Advisory – Business Card</title>
<link rel="stylesheet" href="https://fonts.googleapis.com/css2?family=Open+Sans:ital,wght@0,300;0,400;0,600;0,700;1,400&display=swap">
<style>
  :root {
    --bg: #e9eaec;
    --card: #ffffff;
    --blue: #1ba3d9;
    --blue-dark: #1479ad;
    --blue-light: #5cc4ea;
    --ink: #4a4f55;
    --ink-soft: #8a9096;
    --charcoal: #3a3d41;
    --grey: #b9bdc1;
  }
  * { box-sizing: border-box; margin: 0; padding: 0; }
  html, body { width: 1200px; height: 1000px; overflow: hidden; }
  body {
    background: var(--bg);
    font-family: "Open Sans", Arial, sans-serif;
    position: relative;
  }
  .card {
    position: absolute;
    left: 220px;
    width: 760px;
    height: 434px;
    background: var(--card);
    box-shadow: 0 6px 20px rgba(0,0,0,0.12);
    overflow: hidden;
  }
  .card--front { top: 50px; }
  .card--back { top: 516px; }

  /* brand lockup */
  .brand { display: flex; align-items: center; gap: 14px; }
  .brand__mark { width: 34px; height: 34px; background: var(--blue); flex: none; }
  .brand__name { color: var(--blue); font-weight: 400; font-size: 40px; letter-spacing: -0.5px; line-height: 1; }

  /* front */
  .card--front .brand { position: absolute; left: 60px; top: 120px; }
  .holder { position: absolute; right: 70px; top: 48px; text-align: right; }
  .holder__name { font-size: 24px; font-weight: 700; letter-spacing: 0.5px; color: var(--blue); }
  .holder__name span { color: var(--ink-soft); }
  .holder__title { font-size: 14px; font-weight: 600; color: var(--ink); margin-top: 2px; }
  .corner-tab { position: absolute; right: 0; top: 48px; width: 34px; height: 30px; background: var(--blue); }

  .contact { position: absolute; left: 60px; top: 232px; list-style: none; }
  .contact li { display: flex; align-items: center; gap: 12px; font-size: 15px; font-weight: 300; color: var(--ink-soft); line-height: 26px; }
  .contact svg { width: 14px; height: 14px; flex: none; }

  .tagline-band {
    position: absolute; left: 0; right: 0; bottom: 0; height: 62px;
    background: linear-gradient(100deg, var(--blue-dark) 0%, var(--blue) 45%, var(--blue-light) 75%, var(--blue) 100%);
    display: flex; align-items: center; padding-left: 60px;
  }
  .tagline { color: #fff; font-size: 15px; font-weight: 600; letter-spacing: 3.5px; text-transform: uppercase; }

  /* back */
  .side-strip { position: absolute; left: 0; top: 0; bottom: 0; width: 56px; background: var(--charcoal); }
  .side-strip__accent { position: absolute; left: 0; bottom: 0; width: 56px; height: 120px; background: linear-gradient(180deg, var(--blue-light), var(--blue-dark)); }
  .side-strip__light { position: absolute; left: 56px; top: 0; bottom: 0; width: 10px; background: var(--grey); }
  .card--back .brand { position: absolute; left: 140px; top: 130px; }
  .statement { position: absolute; left: 140px; top: 246px; font-style: italic; font-size: 17px; color: var(--ink); line-height: 30px; }
</style>
</head>
<body>

<section class="card card--front" aria-label="Business card front">
  <div class="brand">
    <span class="brand__mark"></span>
    <span class="brand__name">Hollowmere Advisory LLC</span>
  </div>

  <div class="corner-tab"></div>
  <div class="holder">
    <div class="holder__name">DANIEL <span>MARSH</span></div>
    <div class="holder__title">Ceo/Founder</div>
  </div>

  <ul class="contact">
    <li>
      <svg viewBox="0 0 14 14" aria-hidden="true"><rect x="2" y="1" width="10" height="12" rx="1.5" fill="none" stroke="#8a9096" stroke-width="1.2"/></svg>
      +(123) 4567 890
    </li>
    <li>
      <svg viewBox="0 0 14 14" aria-hidden="true"><path d="M3 1.5l2.2 2.6-1.2 1.6a8 8 0 0 0 4.3 4.3l1.6-1.2 2.6 2.2-1.4 1.5C6.5 12.5 1.5 7.5 1.5 3z" fill="none" stroke="#1ba3d9" stroke-width="1.2" stroke-linejoin="round"/></svg>
      +(123) 4567 890
    </li>
    <li>
      <svg viewBox="0 0 14 14" aria-hidden="true"><rect x="1" y="3" width="12" height="9" fill="none" stroke="#8a9096" stroke-width="1.2"/><path d="M1 3l6 5 6-5" fill="none" stroke="#8a9096" stroke-width="1.2"/></svg>
      person@HollowmereAdvisory.com
    </li>
  </ul>

  <div class="tagline-band">
    <span class="tagline">Optimize Your Investment in Talent</span>
  </div>
</section>

<section class="card card--back" aria-label="Business card back">
  <div class="side-strip"><div class="side-strip__accent"></div></div>
  <div class="side-strip__light"></div>

  <div class="brand">
    <span class="brand__mark"></span>
    <span class="brand__name">Hollowmere Advisory LLC</span>
  </div>

  <p class="statement">
    Growth is Imperative. Change is constant. Talent executes strategy.<br>
    We help you excel at all three
  </p>
</section>

</body>
</html>
```